Bref créative
Biz Card for a Professional Organizer
Dana Kowalt
Cutting-Edge
Room Clearing Maestro
Serving the Bay Area
info@42plumova.com
www.42plumova.com
I'd like a clean design, possibly going vertical instead of the traditional horizontal-UNLESS it is just going to look better going horizontal.
I'm open to suggestions here. I also have black and white versions of my logo if that would work well here...
black version of logo
reverse version of logo
color version

```html
<!DOCTYPE html>
<html lang="en">
<head>
<meta charset="utf-8">
<title>42 Plumova Stationery</title>
<link href="https://fonts.googleapis.com/css2?family=Montserrat:wght@400;600;800&display=swap" rel="stylesheet">
<style>
:root{
  --stage:#d8c3a0;
  --paper:#ffffff;
  --teal:#2f6f88;
  --teal-light:#4d8ea6;
  --brown:#7b4a34;
  --ink:#5a6770;
  --faint:#e4ecf0;
  --label:#6b5a44;
}
*{margin:0;padding:0;box-sizing:border-box}
html,body{width:1200px;height:422px;overflow:hidden}
body{background:var(--stage);font-family:"Montserrat",sans-serif;position:relative}
.sheet{position:absolute;background:var(--paper);box-shadow:0 2px 6px rgba(0,0,0,.18);overflow:hidden}
.brand{font-weight:800;color:var(--teal);white-space:nowrap;line-height:1}
.faint-mark{position:absolute;font-weight:800;color:var(--faint);line-height:1}
.label{position:absolute;font-size:7px;color:var(--label);letter-spacing:.5px;text-transform:uppercase;white-space:nowrap}
.section-title{left:12px;top:80px}
.small{font-size:5px;color:var(--ink);line-height:1.6}

/* business cards */
.card{top:96px;width:60px;height:138px}
.card-front{left:12px}
.card-back{left:77px;background:var(--teal)}
.card .brand{position:absolute;left:0;right:0;top:14px;text-align:center;font-size:10px;line-height:1.15;white-space:normal}
.card-front .band{position:absolute;left:0;right:0;bottom:0;height:52px;background:var(--teal)}
.card-back .brand{color:var(--paper)}
.card-back .small{position:absolute;left:6px;right:4px;bottom:14px;color:var(--paper);font-size:4.5px}
.card-front-label{left:12px;top:240px}
.card-back-label{left:77px;top:240px}

/* letterheads */
.letterhead{top:12px;width:276px;height:384px}
.letter-one{left:216px}
.letter-two{left:516px}
.letterhead .brand{position:absolute;left:16px;top:22px;font-size:20px}
.letter-two .brand{left:0;right:0;text-align:center}
.letterhead .contact{position:absolute;right:16px;top:24px;text-align:right}
.letter-two .contact{left:0;right:0;top:auto;bottom:18px;text-align:center}
.letterhead .band{position:absolute;left:0;right:0;bottom:8px;height:5px;background:var(--teal)}
.letterhead .faint-mark{right:10px;bottom:20px;font-size:120px}
.letter-one-label{left:300px;top:406px}
.letter-two-label{left:600px;top:406px}

/* envelopes */
.envelope{left:828px;width:360px}
.env-blue{top:24px;height:84px;background:var(--teal)}
.env-brown{top:120px;height:84px;background:var(--brown)}
.env-white{top:211px;height:77px}
.envelope svg{position:absolute;left:0;top:0}
.envelope .brand{position:absolute;left:0;right:0;top:30px;text-align:center;font-size:16px;color:var(--paper)}
.env-white .brand{color:var(--teal);top:28px}
.env-dl{left:828px;top:312px;width:360px;height:84px}
.env-dl .brand{position:absolute;left:14px;top:12px;font-size:14px}
.env-dl .small{position:absolute;left:14px;top:32px}
.env-dl .faint-mark{right:10px;bottom:-8px;font-size:70px}
.envelope-label{left:960px;top:400px}
</style>
</head>
<body>
<div class="label section-title">Stationery Concepts</div>

<div class="sheet card card-front">
  <div class="brand">42<br>Plumova</div>
  <div class="band"></div>
</div>
<div class="sheet card card-back">
  <div class="brand">42<br>Plumova</div>
  <div class="small">Dana Kowalt<br>Room Clearing Maestro<br>info@42plumova.com</div>
</div>
<div class="label card-front-label">Card Front</div>
<div class="label card-back-label">Card Back</div>

<div class="sheet letterhead letter-one">
  <div class="brand">42 Plumova</div>
  <div class="small contact">info@42plumova.com<br>www.42plumova.com<br>42_Plumova</div>
  <div class="faint-mark">42</div>
  <div class="band"></div>
</div>
<div class="sheet letterhead letter-two">
  <div class="brand">42 Plumova</div>
  <div class="faint-mark">42</div>
  <div class="small contact">info@42plumova.com · www.42plumova.com · 42_Plumova</div>
  <div class="band"></div>
</div>
<div class="label letter-one-label">Letter Head Option 1</div>
<div class="label letter-two-label">Letter Head Option 2</div>

<div class="sheet envelope env-blue">
  <div class="brand">42 Plumova</div>
</div>
<div class="sheet envelope env-brown">
  <div class="brand">42 Plumova</div>
</div>
<div class="sheet envelope env-white">
  <svg width="360" height="77" viewBox="0 0 360 77"><path d="M0 0 L180 40 L360 0" fill="none" stroke="#d6dde2" stroke-width="1"/></svg>
  <div class="brand">42 Plumova</div>
</div>
<div class="sheet env-dl">
  <div class="brand">42 Plumova</div>
  <div class="small">Serving the Bay Area</div>
  <div class="faint-mark">42</div>
</div>
<div class="label envelope-label">Envelope Options</div>
</body>
</html>
```